Copper lark buildworks

Copper lark buildworks is a small construction company.
Who is a licenced builder, Carpenter, joiner,
working on heritage ,new build, speacial projects and sometimes furniture

Industry/Entity Type

Construction

```html
<!DOCTYPE html>
<html lang="en">
<head>
<meta charset="utf-8">
<title>Copper lark buildworks – business card</title>
<link rel="stylesheet" href="https://fonts.googleapis.com/css2?family=Arimo&family=Fira+Sans&family=Libre+Baskerville:ital,wght@1,700&family=Questrial&family=Roboto+Condensed:wght@300&display=swap">
<style>
  :root {
    --leaf: #8aac3f;
    --charcoal: #353334;
    --paper: #ffffff;
    --edge: #d6d6d6;
    --ink-light: #ffffff;
  }
  * { box-sizing: border-box; margin: 0; padding: 0; }
  html, body {
    width: 1200px;
    height: 734px;
    overflow: hidden;
    background: var(--paper);
  }
  .card {
    position: absolute;
    left: 69px;
    top: 63px;
    width: 1050px;
    height: 600px;
    border-radius: 26px;
    overflow: hidden;
    border: 1px solid var(--edge);
    background: var(--paper);
  }
  .accent-band {
    position: absolute;
    left: 0; top: 0;
    width: 100%;
    height: 39px;
    background: var(--leaf);
  }
  .main-panel {
    position: absolute;
    left: 0; top: 39px;
    width: 100%;
    height: 458px;
    background: var(--charcoal);
  }
  .brand {
    position: absolute;
    left: 40px;
    top: 150px;
    width: 496px;
    text-align: center;
    font-family: "Questrial", sans-serif;
    font-size: 44px;
    line-height: 1.15;
    letter-spacing: 6px;
    color: var(--leaf);
    text-transform: uppercase;
  }
  .divider {
    position: absolute;
    left: 555px;
    top: 92px;
    width: 2px;
    height: 233px;
    background: var(--ink-light);
  }
  .contact-name {
    position: absolute;
    left: 642px;
    top: 100px;
    width: 300px;
    text-align: center;
    font-family: "Libre Baskerville", serif;
    font-style: italic;
    font-weight: 700;
    font-size: 40px;
    color: var(--leaf);
  }
  .contact-phone {
    position: absolute;
    left: 718px;
    top: 165px;
    display: flex;
    align-items: center;
    gap: 14px;
    font-family: "Arimo", sans-serif;
    font-size: 31px;
    color: var(--ink-light);
  }
  .contact-phone svg { width: 27px; height: 27px; }
  .services {
    position: absolute;
    left: 0;
    top: 356px;
    width: 100%;
    text-align: center;
    font-family: "Fira Sans", sans-serif;
    font-size: 27.5px;
    line-height: 38px;
    color: var(--ink-light);
  }
  .footer {
    position: absolute;
    left: 0;
    top: 497px;
    width: 100%;
    height: 103px;
    display: flex;
    align-items: center;
    justify-content: center;
    gap: 30px;
    font-family: "Roboto Condensed", sans-serif;
    font-weight: 300;
    font-size: 35px;
    color: var(--leaf);
  }
  .footer .sep { font-size: 32px; }
  .social-slot {
    width: 34px;
    height: 34px;
    background: var(--leaf);
    border-radius: 3px;
  }
</style>
</head>
<body>
  <div class="card">
    <div class="accent-band"></div>
    <div class="main-panel">
      <div class="brand">Copper Lark<br>Buildworks</div>
      <div class="divider"></div>
      <div class="contact-name">Marcus Hale</div>
      <div class="contact-phone">
        <svg viewBox="0 0 24 24" aria-hidden="true">
          <circle cx="12" cy="12" r="12" fill="#ffffff"/>
          <path d="M8.2 6.2c.4-.3.9-.2 1.1.2l1.2 2.1c.2.4.1.8-.2 1.1l-.8.7c.6 1.4 1.7 2.6 3.1 3.3l.7-.8c.3-.3.8-.4 1.1-.2l2.1 1.2c.4.2.5.8.2 1.1l-.9 1.1c-.5.6-1.3.8-2 .5-3.1-1.2-5.5-3.6-6.7-6.7-.3-.7-.1-1.5.5-2z" fill="#353334"/>
        </svg>
        <span>0491570156</span>
      </div>
      <p class="services">licenced builder, Carpenter, joiner, working on heritage ,new build,<br>special projects and sometimes furniture</p>
    </div>
    <div class="footer">
      <span class="web">www.yourwebsite.com</span>
      <span class="sep">|</span>
      <span class="mail">E: info@youremail.com</span>
      <span class="sep">|</span>
      <span class="social-slot" role="img" aria-label="Social profile link"></span>
      <span class="sep">|</span>
      <span class="social-slot" role="img" aria-label="Social profile link"></span>
    </div>
  </div>
</body>
</html>
```